Needed Box Packaging: Dog XL Puppy Pee/Poo Pads

We're looking for a creative and fun design for our XL puppy pads. Attached is all the documents you will need.

Our pads are unique with Bamboo Charcoal and optional Adhesive sticker backing on the corners. 23" x 35" is the size. There's 50 per box.

ABSORBS 2x as much, 2x as fast, so you never come home to ruined floors
BLACK puppy pads, so your pets mess stays discrete and you never see a yellow stain on a white puppy pad in your home
ODOR ELIMINATION with carbon technology for all-day use to ensure your home stays fresh
LEAK PROOF Tidewell Polymer turns liquid into gel instantly to guarantee dry floors and easy clean up
PHEROMONE ATTRACTION to ensure pets feel comfortable and knows to hit the right spot every time

Target Market(s)

Dog owners

Font styles to use
Sans Serif

Colors
33a6d7
33b8a4
acd036
fbee3d
faa54b

Requirements
Must have
• Must have logo, size of pads, benefits, UPC code, number packed per box, pictures of a dog and picture of the pads
Should not have
• cats

```html
<!DOCTYPE html>
<html lang="en">
<head>
<meta charset="utf-8">
<title>Bamboo Charcoal Training Pads – Front Panel</title>
<link rel="stylesheet" href="https://fonts.googleapis.com/css2?family=Oswald:wght@400;500;600&display=swap">
<style>
  :root {
    --backdrop: #eeeeee;
    --teal-light: #6fe3d8;
    --teal: #3fcfc6;
    --teal-deep: #2fb7b6;
    --ink: #ffffff;
    --brand-ink: #3a211b;
    --ribbon: #d8232f;
    --ribbon-dark: #a3141f;
    --puppy-dark: #3b2016;
    --puppy-mid: #6b3a26;
    --pad-white: #f4f8fa;
    --pad-blue: #8fd7ea;
  }
  * { box-sizing: border-box; margin: 0; padding: 0; }
  html, body { width: 1200px; height: 850px; overflow: hidden; }
  body {
    background: var(--backdrop);
    font-family: "Oswald", "Arial Narrow", sans-serif;
    display: flex; align-items: center; justify-content: center;
  }
  .front-panel {
    position: relative;
    width: 500px; height: 760px;
    background: linear-gradient(180deg, var(--teal-light) 0%, var(--teal) 45%, var(--teal-deep) 100%);
    color: var(--ink);
    overflow: hidden;
  }
  .brand {
    position: absolute; top: 110px; left: 0; right: 0;
    display: flex; flex-direction: column; align-items: center; gap: 10px;
  }
  .brand-dot {
    width: 96px; height: 96px; border-radius: 50%;
    background: var(--ink); border: 3px solid var(--brand-ink);
  }
  .brand-name {
    font-size: 22px; font-weight: 500; letter-spacing: 3px; color: var(--brand-ink);
  }
  .product-title {
    position: absolute; top: 268px; left: 0; right: 0;
    text-align: center; font-weight: 600; font-size: 38px; line-height: 1.05;
    letter-spacing: 0.5px; text-transform: uppercase;
  }
  .ribbon {
    position: absolute; top: 378px; left: 50%; transform: translateX(-50%) rotate(4deg);
    width: 200px; height: 40px;
    background: var(--ribbon);
    box-shadow: -10px 6px 0 var(--ribbon-dark), 10px 6px 0 var(--ribbon-dark);
    display: flex; align-items: center; justify-content: center;
    font-size: 17px; font-weight: 500; letter-spacing: 0.5px;
  }
  .benefits {
    position: absolute; top: 450px; left: 0; right: 0;
    display: flex; justify-content: center; gap: 34px;
  }
  .benefit { width: 90px; text-align: center; font-size: 11px; line-height: 1.15; text-transform: uppercase; }
  .benefit svg { display: block; margin: 0 auto 6px; }
  .claim {
    position: absolute; top: 545px; left: 196px; width: 230px;
    font-size: 12px; line-height: 1.2; text-transform: uppercase; transform: rotate(4deg);
  }
  .puppy-photo {
    position: absolute; left: 0; bottom: 30px; width: 190px; height: 190px;
    background: radial-gradient(circle at 55% 40%, var(--puppy-mid), var(--puppy-dark) 70%);
    border-radius: 50% 50% 0 0;
  }
  .pad-photo {
    position: absolute; left: 222px; bottom: 46px; width: 120px; height: 120px;
    border-radius: 50%;
    background: linear-gradient(145deg, var(--pad-white) 40%, var(--pad-blue));
  }
  .pad-caption {
    position: absolute; left: 202px; bottom: 22px; width: 160px;
    text-align: center; font-size: 10px; text-transform: uppercase;
  }
  .pad-layers {
    position: absolute; left: 210px; top: 690px;
    font-size: 9px; line-height: 1; white-space: nowrap;
    text-transform: uppercase;
    transform-origin: left top; transform: rotate(-72deg);
  }
  .count-box {
    position: absolute; right: 28px; bottom: 24px; width: 92px; height: 118px;
    border: 3px solid var(--ink); border-radius: 4px;
    display: flex; flex-direction: column; align-items: center; justify-content: center;
    line-height: 0.95;
  }
  .count-number { font-size: 60px; font-weight: 600; }
  .count-unit { font-size: 26px; font-weight: 500; }
</style>
</head>
<body>
  <main class="front-panel">
    <div class="brand">
      <span class="brand-dot"></span>
      <span class="brand-name">PAWMORA</span>
    </div>

    <h1 class="product-title">Bamboo Charcoal<br>Training Pads</h1>

    <div class="ribbon">BLACK PUPPY PADS</div>

    <section class="benefits">
      <div class="benefit">
        <svg width="44" height="44" viewBox="0 0 44 44" fill="none" stroke="#fff" stroke-width="2">
          <circle cx="22" cy="22" r="20"/>
          <circle cx="22" cy="24" r="8"/>
          <path d="M19 14h6M22 14v2M8 36L36 8"/>
        </svg>
        Pheromone<br>Attraction
      </div>
      <div class="benefit">
        <svg width="44" height="44" viewBox="0 0 44 44" fill="none" stroke="#fff" stroke-width="2">
          <circle cx="22" cy="22" r="20"/>
          <path d="M20 10c-2 8-6 14-6 18a5 5 0 0 0 10 2M26 30c2-1 4 0 4 2M8 36L36 8"/>
        </svg>
        Odor Elimination
      </div>
      <div class="benefit">
        <svg width="44" height="44" viewBox="0 0 44 44" fill="none" stroke="#fff" stroke-width="2">
          <circle cx="22" cy="22" r="20"/>
          <path d="M22 9c-5 8-9 12-9 17a9 9 0 0 0 18 0c0-5-4-9-9-17z" fill="#fff"/>
        </svg>
        Leak Proof
      </div>
    </section>

    <p class="claim">With activate carbon technology,<br>absorbs 2x as much, 2x as fast</p>

    <div class="puppy-photo" role="img" aria-label="Photo of two chocolate labrador puppies lying together"></div>

    <span class="pad-layers">5 layer composition</span>
    <div class="pad-photo" role="img" aria-label="Photo of a folded training pad"></div>
    <p class="pad-caption">23" x 35" size</p>

    <div class="count-box">
      <span class="count-number">50</span>
      <span class="count-unit">PADS</span>
    </div>
  </main>
</body>
</html>
```